Avocado Wholesale Fruit Box Design (Contest)

We are a wholesale fruit distributing company and we have to create our own Avocado packaging design. We are trying to build a brand around the name "Verdantia". These avocados are from Mexico, and will be mainly exported to the USA. They must accentuate the premium quality we are packing!
Go crazy, make it as wild or as conservative as you want. Let's see what you can come up with!

Target Market(s)
Wholesales, Importers, Distributors
Industry/Entity Type
Agribusiness
Colors
a54499
9ecc3e
fbed22
Requirements
Must have
- -Please use the adobe files with the blank base/measurements as a mold.
-Electric purple background (box will be electric purple color). See attachment of the purple tone we are looking for.
-Must include the word (our brand): "Verdantia". This should be in yellow font and green outline (see attachment of green tone we are looking for). The font and design is for you guys to decide.
-Must include our logo (please find it on the attachments).
-Must include "Imported by Bruma Traders Las Vegas NV USA". The Bruma Traders portion must use the font/color as seen in our attached logo.
-Must include "Produce of Mexico".
-Must include "Premium hass avocados".
-Must include "Net Weight 25 lbs / 11.2 kg.
-Must include "www.brumatraders-example.com".
-3 colors only: Bruma Traders green, hot purple, and yellow.
-Must include a checkbox for the different avocado count inside the box. These are all the avocado count 24,28,32,36,40,48,60,70, and 84. Be creative with this one (please see attachments for a reference).
Nice to have
- -pick a nice yellow tone that will combine with the other two colors (green and yellow).

Should not have
- -It should not have the colors from the color wheel.
-See attachments of the specific colors we are looking for

```html
<!DOCTYPE html>
<html lang="en">
<head>
<meta charset="utf-8">
<title>Verdantia Avocado Carton Box Design</title>
<link rel="stylesheet" href="https://fonts.googleapis.com/css2?family=Fredoka:wght@600;700&family=Great+Vibes&family=Arimo:wght@400;700&display=swap">
<style>
  :root {
    --purple: #ae36f5;
    --lime: #c0ea4b;
    --yellow: #fbed22;
    --navy: #0a1a7a;
    --cut: #2a1040;
    --fold: #e0203a;
    --ink: #111;
    --paper: #ffffff;
  }
  html, body { margin: 0; padding: 0; overflow: hidden; background: var(--paper); }
  .board { display: block; width: 1200px; height: 1026px; }
  .board-fill { fill: var(--purple); }
  .cut { fill: none; stroke: var(--cut); stroke-width: 2; }
  .fold { fill: none; stroke: var(--fold); stroke-width: 1.5; stroke-dasharray: 8 5; }
  .hole { fill: none; stroke: var(--cut); stroke-width: 2; }
  .brand { font-family: 'Fredoka', sans-serif; font-weight: 700; fill: var(--lime); }
  .slogan { font-family: 'Fredoka', sans-serif; font-weight: 700; fill: var(--lime); font-style: normal; }
  .script { font-family: 'Great Vibes', cursive; fill: var(--yellow); }
  .info { font-family: 'Arimo', sans-serif; font-weight: 700; fill: var(--yellow); }
  .small { font-family: 'Arimo', sans-serif; fill: var(--yellow); }
  .importer-name { font-family: 'Arimo', sans-serif; font-weight: 700; fill: var(--lime); }
  .checkbox { fill: none; stroke: var(--yellow); stroke-width: 1.3; }
  .origin-badge { fill: none; stroke: var(--lime); stroke-width: 2.5; }
  .dim-line { stroke: var(--navy); stroke-width: 1.2; fill: none; }
  .dim-guide { stroke: var(--navy); stroke-width: 0.8; fill: none; }
  .dim-arrow { fill: var(--navy); }
  .dim-text { font-family: 'Arimo', sans-serif; font-size: 40px; fill: var(--navy); }
  .view-label { font-family: 'Arimo', sans-serif; font-weight: 700; font-size: 40px; fill: var(--ink); }
  .spec-label { font-family: 'Arimo', sans-serif; font-weight: 700; font-size: 38px; fill: var(--ink); }
  .spec-value { font-family: 'Arimo', sans-serif; font-weight: 400; font-size: 38px; fill: var(--ink); }
  .swatch-hex { font-family: 'Arimo', sans-serif; font-weight: 700; font-size: 32px; fill: var(--ink); }
  .sticker-label { font-family: 'Arimo', sans-serif; font-weight: 700; font-size: 32px; fill: var(--ink); }
  .swatch-purple { fill: var(--purple); }
  .swatch-lime { fill: var(--lime); }
  .swatch-yellow { fill: var(--yellow); }
  .sticker-ring { fill: var(--lime); }
  .sticker-face { fill: var(--purple); }
  .view-fill { fill: var(--purple); }
  .notch { fill: none; stroke: var(--cut); stroke-width: 2; }
</style>
</head>
<body>
<svg class="board" viewBox="0 0 2048 1751" xmlns="http://www.w3.org/2000/svg">
  <defs>
    <!-- upper half of the main dieline print; the lower half is the same group turned 180° -->
    <g id="panel-half">
      <text class="slogan" x="592" y="305" font-size="36" text-anchor="middle">Always</text>
      <text class="slogan" x="608" y="335" font-size="36" text-anchor="middle">Delicious</text>
      <circle class="hole" cx="483" cy="274" r="15"/>
      <circle class="hole" cx="700" cy="274" r="15"/>
      <rect class="hole" x="376" y="262" width="9" height="46" rx="4"/>
      <rect class="hole" x="799" y="262" width="9" height="46" rx="4"/>
      <rect class="hole" x="482" y="358" width="63" height="40" rx="12"/>
      <rect class="hole" x="640" y="358" width="63" height="40" rx="12"/>
      <rect class="hole" x="482" y="545" width="63" height="40" rx="12"/>
      <rect class="hole" x="640" y="545" width="63" height="40" rx="12"/>
      <text class="brand" x="592" y="492" font-size="60" text-anchor="middle">Verdantia</text>
      <text class="script" x="592" y="517" font-size="22" text-anchor="middle">Premium Hass Avocados</text>
      <rect class="hole" x="447" y="447" width="15" height="46" rx="7"/>
      <rect class="hole" x="721" y="447" width="15" height="46" rx="7"/>
      <rect class="hole" x="279" y="447" width="26" height="48" rx="12"/>
      <rect class="hole" x="879" y="447" width="26" height="48" rx="12"/>
      <path class="cut" d="M222 562 V380 H263 Q263 360 283 360 H298 Q318 360 318 380 H380"/>
      <path class="cut" d="M962 562 V380 H920 Q920 360 900 360 H885 Q865 360 865 380 H803"/>
      <path class="cut" d="M222 562 H263 Q263 548 283 548 H298 Q318 548 318 562 H380"/>
      <path class="cut" d="M962 562 H920 Q920 548 900 548 H885 Q865 548 865 562 H803"/>
    </g>

    <!-- left side panel print; right panel is the same group turned 180° -->
    <g id="side-half">
      <text class="brand" font-size="46" text-anchor="middle" transform="translate(248 732) rotate(-90)">Verdantia</text>
      <text class="script" font-size="17" text-anchor="middle" transform="translate(263 732) rotate(-90)">Premium Hass Avocados</text>
      <text class="info" font-size="9" transform="translate(266 632) rotate(-90)">Category 1</text>
      <text class="info" font-size="9" transform="translate(276 632) rotate(-90)">Count</text>
      <g class="count-boxes">
        <rect class="checkbox" x="280" y="621" width="10" height="10"/>
        <rect class="checkbox" x="294" y="621" width="10" height="10"/>
        <rect class="checkbox" x="308" y="621" width="10" height="10"/>
        <rect class="checkbox" x="322" y="621" width="10" height="10"/>
        <rect class="checkbox" x="336" y="621" width="10" height="10"/>
        <rect class="checkbox" x="280" y="596" width="10" height="10"/>
        <rect class="checkbox" x="294" y="596" width="10" height="10"/>
        <rect class="checkbox" x="308" y="596" width="10" height="10"/>
        <rect class="checkbox" x="322" y="596" width="10" height="10"/>
        <text class="info" font-size="8" transform="translate(289 618) rotate(-90)">24</text>
        <text class="info" font-size="8" transform="translate(303 618) rotate(-90)">28</text>
        <text class="info" font-size="8" transform="translate(317 618) rotate(-90)">32</text>
        <text class="info" font-size="8" transform="translate(331 618) rotate(-90)">36</text>
        <text class="info" font-size="8" transform="translate(345 618) rotate(-90)">40</text>
        <text class="info" font-size="8" transform="translate(289 593) rotate(-90)">48</text>
        <text class="info" font-size="8" transform="translate(303 593) rotate(-90)">60</text>
        <text class="info" font-size="8" transform="translate(317 593) rotate(-90)">70</text>
        <text class="info" font-size="8" transform="translate(331 593) rotate(-90)">84</text>
      </g>
      <rect class="hole" x="266" y="642" width="34" height="18" rx="9"/>
      <rect class="hole" x="266" y="802" width="34" height="18" rx="9"/>
      <text class="info" font-size="11" transform="translate(268 878) rotate(-90)">Net Wt.</text>
      <text class="info" font-size="11" transform="translate(280 878) rotate(-90)">11.2 kg</text>
      <text class="info" font-size="11" transform="translate(292 878) rotate(-90)">25 lbs</text>
      <ellipse class="origin-badge" cx="343" cy="856" rx="13" ry="21"/>
      <text class="importer-name" font-size="12" text-anchor="middle" transform="translate(322 730) rotate(-90)">Bruma Traders</text>
      <text class="small" font-size="6" text-anchor="middle" transform="translate(331 730) rotate(-90)">www.brumatraders-example.com</text>
      <text class="small" font-size="8" text-anchor="middle" transform="translate(341 730) rotate(-90)">Imported by</text>
      <text class="small" font-size="8" text-anchor="middle" transform="translate(351 730) rotate(-90)">Bruma Traders Las Vegas NV USA</text>
      <path class="cut" d="M390 625 H370 Q360 625 360 640 V668 Q360 682 370 682 H390"/>
      <path class="cut" d="M390 780 H370 Q360 780 360 795 V823 Q360 838 370 838 H390"/>
    </g>

    <g id="lid-slogan">
      <text class="slogan" x="1630" y="452" font-size="38" text-anchor="middle">Always</text>
      <text class="slogan" x="1655" y="485" font-size="38" text-anchor="middle">Delicious</text>
    </g>
  </defs>

  <!-- dimensions -->
  <g class="dimensions">
    <line class="dim-guide" x1="190" y1="170" x2="190" y2="237"/>
    <line class="dim-guide" x1="993" y1="170" x2="993" y2="237"/>
    <line class="dim-line" x1="190" y1="177" x2="525" y2="177"/>
    <line class="dim-line" x1="658" y1="177" x2="993" y2="177"/>
    <path class="dim-arrow" d="M190 177 L213 171 L213 183 Z"/>
    <path class="dim-arrow" d="M993 177 L970 171 L970 183 Z"/>
    <text class="dim-text" x="592" y="192" text-anchor="middle">795mm</text>
    <line class="dim-guide" x1="993" y1="237" x2="1088" y2="237"/>
    <line class="dim-guide" x1="993" y1="1226" x2="1088" y2="1226"/>
    <line class="dim-line" x1="1080" y1="237" x2="1080" y2="705"/>
    <line class="dim-line" x1="1080" y1="760" x2="1080" y2="1226"/>
    <path class="dim-arrow" d="M1080 237 L1074 260 L1086 260 Z"/>
    <path class="dim-arrow" d="M1080 1226 L1074 1203 L1086 1203 Z"/>
    <text class="dim-text" x="1080" y="747" text-anchor="middle">980mm</text>
  </g>

  <!-- dieline -->
  <g class="dieline">
    <rect class="board-fill" x="190" y="237" width="803" height="989"/>
    <path class="cut" d="M365 237 H818 V380 M365 237 V380 M365 1226 H818 V1084 M365 1226 V1084"/>
    <rect class="cut" x="190" y="572" width="803" height="318"/>
    <line class="fold" x1="380" y1="378" x2="803" y2="378"/>
    <line class="fold" x1="380" y1="564" x2="803" y2="564"/>
    <line class="fold" x1="380" y1="897" x2="803" y2="897"/>
    <line class="fold" x1="380" y1="1084" x2="803" y2="1084"/>
    <line class="fold" x1="375" y1="378" x2="375" y2="1084"/>
    <line class="fold" x1="803" y1="378" x2="803" y2="1084"/>
    <use href="#panel-half"/>
    <use href="#panel-half" transform="rotate(180 591.5 731.5)"/>
    <use href="#side-half"/>
    <use href="#side-half" transform="rotate(180 591.5 731.5)"/>
    <g class="base-vents">
      <circle class="hole" cx="483" cy="667" r="15"/>
      <circle class="hole" cx="700" cy="667" r="15"/>
      <circle class="hole" cx="424" cy="731" r="15"/>
      <circle class="hole" cx="541" cy="731" r="15"/>
      <circle class="hole" cx="642" cy="731" r="15"/>
      <circle class="hole" cx="760" cy="731" r="15"/>
      <circle class="hole" cx="483" cy="795" r="15"/>
      <circle class="hole" cx="700" cy="795" r="15"/>
    </g>
  </g>

  <!-- top / lid view -->
  <g class="view-lid">
    <rect class="view-fill" x="1401" y="226" width="476" height="309"/>
    <path class="notch" d="M1516 226 V238 Q1516 245 1524 245 H1578 Q1586 245 1586 238 V226"/>
    <path class="notch" d="M1693 226 V238 Q1693 245 1701 245 H1755 Q1763 245 1763 238 V226"/>
    <path class="notch" d="M1516 535 V523 Q1516 516 1524 516 H1578 Q1586 516 1586 523 V535"/>
    <path class="notch" d="M1693 535 V523 Q1693 516 1701 516 H1755 Q1763 516 1763 523 V535"/>
    <circle class="hole" cx="1517" cy="340" r="16"/>
    <circle class="hole" cx="1762" cy="340" r="16"/>
    <circle class="hole" cx="1517" cy="421" r="16"/>
    <circle class="hole" cx="1762" cy="421" r="16"/>
    <use href="#lid-slogan"/>
    <use href="#lid-slogan" transform="rotate(180 1639 380)"/>
    <text class="view-label" x="1639" y="577" text-anchor="middle">Top/ Lid</text>
  </g>

  <!-- front view -->
  <g class="view-front">
    <rect class="view-fill" x="1401" y="649" width="476" height="210"/>
    <path class="notch" d="M1516 649 V661 Q1516 668 1524 668 H1578 Q1586 668 1586 661 V649"/>
    <path class="notch" d="M1693 649 V661 Q1693 668 1701 668 H1755 Q1763 668 1763 661 V649"/>
    <path class="notch" d="M1516 859 V847 Q1516 840 1524 840 H1578 Q1586 840 1586 847 V859"/>
    <path class="notch" d="M1693 859 V847 Q1693 840 1701 840 H1755 Q1763 840 1763 847 V859"/>
    <rect class="hole" x="1477" y="727" width="16" height="50" rx="8"/>
    <rect class="hole" x="1785" y="727" width="16" height="50" rx="8"/>
    <text class="brand" x="1639" y="778" font-size="66" text-anchor="middle">Verdantia</text>
    <text class="script" x="1639" y="804" font-size="24" text-anchor="middle">Premium Hass Avocados</text>
    <text class="view-label" x="1639" y="900" text-anchor="middle">Front</text>
  </g>

  <!-- side view -->
  <g class="view-side">
    <rect class="view-fill" x="1461" y="964" width="356" height="205"/>
    <path class="notch" d="M1501 1169 V1162 Q1501 1153 1512 1153 H1545 Q1556 1153 1556 1162 V1169"/>
    <path class="notch" d="M1722 1169 V1162 Q1722 1153 1733 1153 H1766 Q1777 1153 1777 1162 V1169"/>
    <text class="brand" x="1639" y="1024" font-size="46" text-anchor="middle">Verdantia</text>
    <text class="script" x="1639" y="1041" font-size="16" text-anchor="middle">Premium Hass Avocados</text>
    <text class="info" x="1476" y="1050" font-size="11">Net Wt.</text>
    <text class="info" x="1476" y="1061" font-size="11">11.2 kg</text>
    <text class="info" x="1476" y="1072" font-size="11">25 lbs</text>
    <rect class="hole" x="1540" y="1047" width="19" height="39" rx="9"/>
    <rect class="hole" x="1719" y="1047" width="19" height="39" rx="9"/>
    <text class="info" x="1751" y="1048" font-size="9">Category 1</text>
    <text class="info" x="1751" y="1059" font-size="9">Count</text>
    <g class="count-grid">
      <rect class="checkbox" x="1753" y="1063" width="10" height="10"/><text class="info" x="1765" y="1072" font-size="9">24</text>
      <rect class="checkbox" x="1783" y="1063" width="10" height="10"/><text class="info" x="1795" y="1072" font-size="9">48</text>
      <rect class="checkbox" x="1753" y="1078" width="10" height="10"/><text class="info" x="1765" y="1087" font-size="9">28</text>
      <rect class="checkbox" x="1783" y="1078" width="10" height="10"/><text class="info" x="1795" y="1087" font-size="9">60</text>
      <rect class="checkbox" x="1753" y="1093" width="10" height="10"/><text class="info" x="1765" y="1102" font-size="9">32</text>
      <rect class="checkbox" x="1783" y="1093" width="10" height="10"/><text class="info" x="1795" y="1102" font-size="9">70</text>
      <rect class="checkbox" x="1753" y="1108" width="10" height="10"/><text class="info" x="1765" y="1117" font-size="9">36</text>
      <rect class="checkbox" x="1783" y="1108" width="10" height="10"/><text class="info" x="1795" y="1117" font-size="9">84</text>
      <rect class="checkbox" x="1753" y="1123" width="10" height="10"/><text class="info" x="1765" y="1132" font-size="9">40</text>
    </g>
    <ellipse class="origin-badge" cx="1498" cy="1134" rx="22" ry="14"/>
    <text class="importer-name" x="1639" y="1116" font-size="12" text-anchor="middle">Bruma Traders</text>
    <text class="small" x="1639" y="1126" font-size="6" text-anchor="middle">www.brumatraders-example.com</text>
    <text class="small" x="1639" y="1136" font-size="8" text-anchor="middle">Imported by</text>
    <text class="small" x="1639" y="1145" font-size="8" text-anchor="middle">Bruma Traders Las Vegas NV USA</text>
    <text class="view-label" x="1639" y="1214" text-anchor="middle">Side</text>
  </g>

  <!-- sticker -->
  <g class="sticker">
    <ellipse class="sticker-ring" cx="1640" cy="1398" rx="207" ry="103"/>
    <ellipse class="sticker-face" cx="1640" cy="1398" rx="192" ry="89"/>
    <text class="brand" x="1640" y="1417" font-size="68" text-anchor="middle">Verdantia</text>
    <text class="script" x="1640" y="1448" font-size="24" text-anchor="middle">Premium Hass Avocados</text>
    <text class="sticker-label" x="1644" y="1550" text-anchor="middle">Avocado Sticker</text>
    <text class="sticker-label" x="1640" y="1596" text-anchor="middle">(w:56.739 x h:28.56 px)</text>
  </g>

  <!-- job specification -->
  <g class="job-spec">
    <text x="215" y="1358"><tspan class="spec-label">Job Title: </tspan><tspan class="spec-value">Avocado Carton Box Design</tspan></text>
    <text x="215" y="1413"><tspan class="spec-label">Size: </tspan><tspan class="spec-value">795mm (w) x 980mm (h)</tspan></text>
    <text class="spec-label" x="215" y="1468">Colors:</text>
    <rect class="swatch-purple" x="215" y="1480" width="231" height="81"/>
    <rect class="swatch-lime" x="481" y="1480" width="231" height="81"/>
    <rect class="swatch-yellow" x="747" y="1480" width="231" height="81"/>
    <text class="swatch-hex" x="330" y="1603" text-anchor="middle">#ae36f5</text>
    <text class="swatch-hex" x="596" y="1603" text-anchor="middle">#c0ea4b</text>
    <text class="swatch-hex" x="862" y="1603" text-anchor="middle">#fbed22</text>
  </g>
</svg>
</body>
</html>
```